Business Card Design

We have our logo and everything in place. Looking to have a layout for our new business cards designed. These will be printed with a matte finish, possibly rounded corners, and looking to incorporate some cool spot UV layers into the design.

Ive uploaded the existing card front and back as well as our logo.

Card Size Will Be 3.5" x 2"

```html
<!DOCTYPE html>
<html lang="en">
<head>
<meta charset="utf-8">
<title>Ridgeline Deck Works – Business Card</title>
<link href="https://fonts.googleapis.com/css2?family=Questrial&display=swap" rel="stylesheet">
<style>
  :root {
    --backdrop: #e4e2de;
    --card-top: #1c1c1c;
    --card-bottom: #0b0b0b;
    --ink-white: #f2f2f2;
    --ink-blue: #3b8fd0;
    --ink-silver: #b4b8bd;
    --divider: rgba(255,255,255,0.22);
  }
  * { margin: 0; padding: 0; box-sizing: border-box; }
  html, body {
    width: 1048px; height: 1200px; overflow: hidden;
    background: var(--backdrop);
    font-family: "Questrial", "Helvetica Neue", Arial, sans-serif;
  }
  .canvas { position: relative; width: 1048px; height: 1200px; }
  .card {
    position: absolute; left: 68px; width: 918px; height: 524px;
    border-radius: 46px;
    background: linear-gradient(160deg, var(--card-top) 0%, var(--card-bottom) 100%);
    overflow: hidden; color: var(--ink-white);
  }
  .card--front { top: 48px; }
  .card--back { top: 625px; }

  .front-name {
    position: absolute; left: 0; right: 0; top: 200px;
    text-align: center; font-size: 84px; letter-spacing: 1px; color: var(--ink-white);
  }
  .front-name small {
    display: block; font-size: 30px; letter-spacing: 6px; margin-top: 6px;
  }

  .back-name {
    position: absolute; left: 48px; width: 300px; top: 105px;
    text-align: center; font-size: 50px; line-height: 1; color: var(--ink-silver);
  }
  .back-name small { display: block; font-size: 17px; letter-spacing: 4px; margin-top: 12px; }

  .divider {
    position: absolute; left: 388px; top: 40px; width: 2px; height: 400px;
    background: linear-gradient(180deg, transparent 0%, var(--divider) 45%, rgba(255,255,255,0.35) 75%, transparent 100%);
  }

  .contact { position: absolute; left: 436px; top: 0; }
  .contact__name { position: absolute; top: 90px; white-space: nowrap; font-size: 35px; letter-spacing: 3px; }
  .contact__title { position: absolute; top: 130px; white-space: nowrap; font-size: 26px; letter-spacing: 1px; display: flex; align-items: center; }
  .contact__title::after { content: ""; display: block; width: 135px; height: 2px; background: var(--ink-white); margin-left: 10px; margin-top: 4px; }
  .contact__phone { position: absolute; top: 216px; white-space: nowrap; font-size: 29px; letter-spacing: 3px; }
  .contact__email { position: absolute; top: 264px; white-space: nowrap; font-size: 29px; }
  .contact__web { position: absolute; top: 344px; white-space: nowrap; font-size: 29px; }
  .accent { color: var(--ink-blue); }

  .service-area {
    position: absolute; left: 0; right: 0; top: 456px;
    text-align: center; font-size: 29px; letter-spacing: 2.5px;
  }
</style>
</head>
<body>
<main class="canvas">
  <section class="card card--front" aria-label="Card front">
    <p class="front-name">Ridgeline<small>DECK WORKS</small></p>
  </section>

  <section class="card card--back" aria-label="Card back">
    <p class="back-name">Ridgeline<small>DECK WORKS</small></p>
    <div class="divider"></div>
    <div class="contact">
      <p class="contact__name"><span class="accent">DANIEL</span>MERCER</p>
      <p class="contact__title">president</p>
      <p class="contact__phone">403.555.0187</p>
      <p class="contact__email"><span class="accent">ridgeline</span>deckworks@mail.com</p>
      <p class="contact__web"><span class="accent">ridgeline</span>deckworks.com</p>
    </div>
    <p class="service-area">Serving Calgary and surrounding areas</p>
  </section>
</main>
</body>
</html>
```